Can Design for Fun, Growing Health Food Brand

We are launching a brand new product, electrolyte seltzer drinks. We want the design to be clean/simple and slightly modern while staying true to our brand identity. Must say "Mineral Hydration" as the product descriptor, sub headline is "Carbonated electrolyte beverage with sea moss and real fruit juice". First flavors will be Watermelon Mint and Mango.

Target Market(s)

Women ages 30-50 who are interested in health wellness/trends

Industry/Entity Type

Health & Wellness

Font styles to use
Sans Serif

Requirements
Must have
• Tall, skinny can, current Bright Kelp Co Logo, use aluminum on can as element in design.
Nice to have
• Be fun, clean and modern. Would like to see the label less busy than our gels.
Should not have
• Avoid putting flavor on bottom 1/5 of can. No gradient color changes. Do not want really detailed or realistic fruit image, prefer drawings or similar.

```html
<!DOCTYPE html>
<html lang="en">
<head>
<meta charset="utf-8">
<title>Bright Kelp Co – Watermelon Mint Electrolyte Seltzer</title>
<link href="https://fonts.googleapis.com/css2?family=Oswald:wght@400;600;700&family=Poppins:wght@400;500;600&display=swap" rel="stylesheet">
<style>
  :root {
    --backdrop: #d4d4d4;
    --label-white: #ffffff;
    --kelp-green: #1f4a43;
    --berry-red: #d2434a;
    --band-pink: #f2aeae;
    --band-blush: #f7cfcd;
    --band-rose: #f4bdbb;
    --aluminum-light: #e9e9ea;
    --aluminum-dark: #b9babc;
    --fruit-red: #ef5a5e;
    --rind-green: #3f8f4e;
  }
  * { box-sizing: border-box; margin: 0; padding: 0; }
  html, body { width: 1200px; height: 1200px; overflow: hidden; }
  body {
    background: var(--backdrop);
    font-family: "Poppins", sans-serif;
    position: relative;
  }
  .can-label {
    position: absolute;
    left: 405px; top: 50px;
    width: 390px; height: 1100px;
    background: var(--label-white);
    overflow: hidden;
    border-radius: 14px;
  }
  .aluminum-rim {
    position: absolute; left: 0; width: 100%;
    background: linear-gradient(90deg, var(--aluminum-dark), var(--aluminum-light) 45%, var(--aluminum-dark));
  }
  .aluminum-rim.top { top: 0; height: 22px; }
  .aluminum-rim.bottom { bottom: 0; height: 26px; z-index: 3; }
  .flavor-note-ring {
    position: absolute; top: 26px; width: 100%;
    text-align: center; white-space: nowrap;
    font-family: "Poppins", sans-serif; font-weight: 600; font-style: italic;
    font-size: 13px; letter-spacing: 0.5px; color: var(--berry-red);
  }
  .brand-mark {
    position: absolute; left: 50%; top: 84px;
    width: 70px; height: 70px; margin-left: -35px;
    border: 4px solid var(--kelp-green); border-radius: 50%;
  }
  .brand-name {
    position: absolute; top: 178px; width: 100%;
    text-align: center;
    font-family: "Oswald", sans-serif; font-weight: 400;
    font-size: 50px; letter-spacing: -0.5px;
    color: var(--kelp-green); text-transform: uppercase;
  }
  .flavor-illustration {
    position: absolute; left: 78px; top: 292px;
    width: 248px; height: 156px;
    border-radius: 10px;
    background: linear-gradient(135deg, var(--fruit-red) 0%, var(--fruit-red) 52%, var(--rind-green) 52%, var(--rind-green) 100%);
  }
  .flavor-pill {
    position: absolute; left: 82px; top: 476px;
    width: 240px; height: 41px;
    border: 2px solid var(--berry-red); border-radius: 21px;
    display: flex; align-items: center; justify-content: center;
    font-weight: 500; font-size: 19px; color: var(--berry-red);
  }
  .product-type {
    position: absolute; top: 534px; width: 100%;
    text-align: center; font-weight: 600; font-size: 17px;
    color: var(--kelp-green);
  }
  .product-sub {
    position: absolute; top: 560px; width: 100%;
    text-align: center; font-size: 14px; line-height: 19px;
    color: var(--kelp-green);
  }
  .wave-bands { position: absolute; left: 0; top: 0; width: 390px; height: 1100px; }
  .claims {
    position: absolute; top: 642px; left: 0; width: 100%;
    display: flex; justify-content: center; gap: 38px;
  }
  .claim {
    width: 80px; text-align: center;
    font-weight: 500; font-size: 15px; line-height: 17px;
    color: var(--berry-red); text-transform: uppercase;
  }
  .claim svg { display: block; margin: 0 auto 14px; width: 48px; height: 48px; }
  .descriptor {
    position: absolute; top: 770px; width: 100%;
    text-align: center;
    font-family: "Oswald", sans-serif; font-weight: 700;
    font-size: 70px; line-height: 66px; letter-spacing: 1px;
    color: var(--berry-red); text-transform: uppercase;
  }
  .volume {
    position: absolute; top: 980px; width: 100%;
    text-align: center; font-size: 19px; color: var(--label-white);
  }
</style>
</head>
<body>
  <main class="can-label">
    <div class="aluminum-rim top"></div>
    <div class="flavor-note-ring">NATURALLY FLAVORED /// NATURALLY FLAVORED</div>

    <div class="brand-mark"></div>
    <h1 class="brand-name">Bright Kelp Co</h1>

    <div class="flavor-illustration" role="img" aria-label="Flat drawing of a watermelon wedge with a sprig of mint leaves"></div>

    <div class="flavor-pill">WATERMELON MINT</div>
    <p class="product-type">ELECTROLYTE SELTZER DRINKS</p>
    <p class="product-sub">Carbonated electrolyte beverage<br>with sea moss and real fruit juice</p>

    <svg class="wave-bands" viewBox="0 0 390 1100" aria-hidden="true">
      <path d="M0 674 C90 690 180 660 260 630 C310 612 360 602 390 605 L390 1100 L0 1100 Z" fill="var(--band-blush)"/>
      <path d="M0 800 C60 790 110 750 190 748 C280 746 330 760 390 770 L390 1100 L0 1100 Z" fill="var(--band-rose)"/>
      <path d="M0 875 C80 880 140 900 220 895 C300 890 350 870 390 860 L390 1100 L0 1100 Z" fill="var(--band-pink)"/>
    </svg>

    <div class="claims">
      <div class="claim">
        <svg viewBox="0 0 48 48" fill="none" stroke="var(--berry-red)" stroke-width="2.5" stroke-linecap="round" stroke-linejoin="round">
          <path d="M24 44 V14"/>
          <path d="M24 14 C18 10 18 4 24 2 C30 4 30 10 24 14 Z"/>
          <path d="M24 30 C16 30 10 24 10 18 C18 18 24 22 24 30 Z"/>
          <path d="M24 30 C32 30 38 24 38 18 C30 18 24 22 24 30 Z"/>
        </svg>
        Planted<br>Based
      </div>
      <div class="claim">
        <svg viewBox="0 0 48 48" fill="none" stroke="var(--berry-red)" stroke-width="2.5" stroke-linejoin="round">
          <circle cx="24" cy="24" r="21"/>
          <path d="M16 20 L24 16 L32 20 L32 30 L24 34 L16 30 Z"/>
          <path d="M9 9 L39 39"/>
        </svg>
        Low<br>Sugar
      </div>
      <div class="claim">
        <svg viewBox="0 0 48 48" fill="none" stroke="var(--berry-red)" stroke-width="2.5" stroke-linecap="round">
          <path d="M6 16 C12 12 18 20 24 16 C30 12 36 20 42 16"/>
          <path d="M6 26 C12 22 18 30 24 26 C30 22 36 30 42 26"/>
          <path d="M6 36 C12 32 18 40 24 36 C30 32 36 40 42 36"/>
        </svg>
        Natural<br>Sea Moss
      </div>
    </div>

    <h2 class="descriptor">Mineral<br>Hydration</h2>
    <p class="volume">12 FL OZ (355 mL)</p>

    <div class="aluminum-rim bottom"></div>
  </main>
</body>
</html>
```